2009 Thank You

A colorful post card that is 8.5 x 5.5.  The purpose is to say thank you to our customers and to wish them a prosperous new year.  We a printing company and will print 4-color process on both sides of the post card

• I have included our logo to be incorporated where appropriate 

• The theme might incorporate something that recognizes "these are turbulent times"  or "success from adversity"

```html
<!DOCTYPE html>
<html lang="en">
<head>
<meta charset="utf-8">
<title>2009 Thank You Postcard</title>
<link href="https://fonts.googleapis.com/css2?family=EB+Garamond:ital,wght@0,400;0,600;0,700;1,600&family=Open+Sans:ital,wght@1,600&display=swap" rel="stylesheet">
<style>
  :root {
    --paper: #ffffff;
    --cream: #ece4c4;
    --cream-light: #f0ecd9;
    --slate: #aebfbe;
    --ink: #1b1b1b;
    --caption: #555555;
    --poppy: #d9472b;
    --sage: #9ea56b;
    --ochre: #8d7432;
    --stamp-line: #9fb3b8;
  }
  * { margin: 0; padding: 0; box-sizing: border-box; }
  html, body { width: 927px; height: 1200px; overflow: hidden; background: var(--paper); }
  body { position: relative; font-family: "EB Garamond", Georgia, serif; color: var(--ink); }

  .card { position: absolute; left: 114px; width: 690px; height: 447px; overflow: hidden; }
  .card--front { top: 94px; background: var(--cream); }
  .card--back { top: 634px; display: flex; }

  .ornament { position: absolute; }
  .ornament--poppies { left: 40px; top: 0; width: 210px; height: 190px;
    background: radial-gradient(ellipse at center, rgba(217,71,43,.85) 0%, rgba(217,71,43,.45) 45%, rgba(217,71,43,0) 72%); }
  .ornament--sage-flower { left: 120px; top: 130px; width: 345px; height: 300px;
    background: radial-gradient(ellipse at center, rgba(158,165,107,.95) 0%, rgba(158,165,107,.55) 40%, rgba(158,165,107,0) 70%); }
  .ornament--gold-vine { left: -30px; top: 135px; width: 300px; height: 340px;
    background: radial-gradient(ellipse at 35% 70%, rgba(141,116,50,.85) 0%, rgba(141,116,50,.4) 42%, rgba(141,116,50,0) 70%); }
  .ornament--gold-scroll { left: 485px; top: -40px; width: 240px; height: 210px;
    background: radial-gradient(ellipse at 70% 45%, rgba(141,116,50,.8) 0%, rgba(141,116,50,.35) 45%, rgba(141,116,50,0) 72%); }

  .quote-band { position: absolute; left: 0; top: 61px; width: 100%; height: 72px; background: var(--slate); opacity: .97; }
  .quote-band__text { position: absolute; left: 112px; top: 17px; font-weight: 700; font-variant: small-caps; font-size: 15px; letter-spacing: .3px; }
  .quote-band__author { position: absolute; right: 84px; top: 36px; font-style: italic; font-weight: 600; font-size: 14px; }

  .brand { position: absolute; text-align: left; }
  .brand__name { font-family: "EB Garamond", Georgia, serif; font-weight: 700; font-size: 31px; line-height: 1; color: var(--ink); letter-spacing: -.3px; }
  .brand__tagline { font-family: "Open Sans", Arial, sans-serif; font-style: italic; font-weight: 600; font-size: 6.2px; color: var(--ink); margin-top: 5px; }
  .card--front .brand { right: 25px; top: 383px; }

  .card__message { position: relative; width: 406px; height: 100%; background: var(--slate); }
  .ornament--back-vines { left: 0; top: 0; width: 150px; height: 447px;
    background: linear-gradient(180deg, rgba(200,214,212,.6), rgba(200,214,212,.25) 50%, rgba(200,214,212,.55)); }
  .ornament--back-poppy { left: 316px; top: 208px; width: 110px; height: 150px;
    background: radial-gradient(ellipse at 80% 50%, rgba(217,71,43,.9) 0%, rgba(217,71,43,.45) 40%, rgba(217,71,43,0) 70%); }

  .message { position: absolute; left: 0; width: 406px; top: 68px; text-align: center; font-size: 12.4px; line-height: 15.6px; }
  .message p { margin-bottom: 16px; }
  .message .lead { font-weight: 700; font-variant: small-caps; letter-spacing: .2px; }
  .card--back .brand { left: 118px; top: 293px; }
  .contact { position: absolute; left: 0; width: 406px; top: 370px; text-align: center; font-size: 12.8px; line-height: 16.6px; }

  .card__address { position: relative; flex: 1; background: var(--cream-light); }
  .stamp-box { position: absolute; left: 202px; top: 28px; width: 53px; height: 54px; border: 1px solid var(--stamp-line); }
  .ornament--faint-blooms { left: 100px; top: 320px; width: 190px; height: 130px;
    background: radial-gradient(ellipse at 60% 60%, rgba(222,216,190,.9) 0%, rgba(222,216,190,0) 70%); }

  .caption { position: absolute; left: 0; width: 927px; text-align: center; font-size: 19px; color: var(--caption); }
  .caption--front { top: 560px; }
  .caption--back { top: 1098px; }
</style>
</head>
<body>
  <section class="card card--front" aria-label="Postcard front">
    <div class="ornament ornament--poppies" role="img" aria-label="Red stencil flowers"></div>
    <div class="ornament ornament--gold-vine" role="img" aria-label="Gold curling vine with small blossoms"></div>
    <div class="ornament ornament--sage-flower" role="img" aria-label="Large sage-green stylised flower"></div>
    <div class="ornament ornament--gold-scroll" role="img" aria-label="Gold scrollwork flourish"></div>
    <div class="quote-band">
      <p class="quote-band__text">"The essence of all beautiful art, all great art, is gratitude."</p>
      <p class="quote-band__author">- Adrian Whitlock</p>
    </div>
    <div class="brand">
      <p class="brand__name">Inkwell Print</p>
      <p class="brand__tagline">printing, marketing, direct mail and fulfillment</p>
    </div>
  </section>
  <p class="caption caption--front">Front</p>

  <section class="card card--back" aria-label="Postcard back">
    <div class="card__message">
      <div class="ornament ornament--back-vines" role="img" aria-label="Faint pale floral vines"></div>
      <div class="ornament ornament--back-poppy" role="img" aria-label="Red stencil flower"></div>
      <div class="message">
        <p><span class="lead">In these turbulent times</span> it’s easy to forget that good things<br>that are happening all around. With this in mind, we just wanted<br>to say thank you for your business in 2008.</p>
        <p><span class="lead">We hope you will enjoy a prosperous</span> year in 2009.<br>If there is anything we can do to help your company succeed,<br>please give us a call. We are happy to provide printing services of all<br>types including brochures, direct mail, multi-media campaigns to<br>drive internet traffic, training materials and fulfillment services.</p>
        <p>Give us a call!</p>
      </div>
      <div class="brand">
        <p class="brand__name">Inkwell Print</p>
        <p class="brand__tagline">printing, marketing, direct mail and fulfillment</p>
      </div>
      <div class="contact">
        <p>2150 Larkspur Ave., Unit #3, Aurora, CO 80011</p>
        <p>Phone Number (303) 555-0142</p>
        <p>www.inkwellprint.com</p>
      </div>
    </div>
    <div class="card__address">
      <div class="stamp-box" aria-label="Stamp area"></div>
      <div class="ornament ornament--faint-blooms" role="img" aria-label="Faint cream blossoms"></div>
    </div>
  </section>
  <p class="caption caption--back">Back</p>
</body>
</html>
```